Would like a design for lawn signs I will be using to advertise with. Attached are three images. One is the jpeg version of our logo to use in creating and editing the design. The other two are mock ups of our current style of tshirt and business card design. I would like the finished product to look similar in style to the mock ups. The actual color of our logo in the jpeg picture is outdated coloring. I would like the logo to be the color of the logo in the mock up tshirt version and the business card design.
The signs I will be using are white in color and 18"x24" white lawn signs, so I would like the logo to appear like the logo in the grey tshirt design, where it is black and orange. As for the text coloring I would like it to be black as well.
The only things I want included on the text of the sign design is:
Phone: 816-402-7761
Email: tidyturfco@fernmail.com
Mowing
Fertilization
Aeration
Bed & tree maintenance
and more.

```html
<!DOCTYPE html>
<html lang="en">
<head>
<meta charset="utf-8">
<title>Tidy Turf Co – Lawn Sign</title>
<link rel="stylesheet" href="https://fonts.googleapis.com/css2?family=Open+Sans:wght@700&display=swap">
<style>
  :root {
    --canvas-bg: #ffffff;
    --sign-bg: #ffffff;
    --ink: #231f20;
    --accent: #e4432a;
    --shadow: rgba(0, 0, 0, 0.55);
  }
  html, body {
    margin: 0;
    padding: 0;
    width: 1200px;
    height: 1000px;
    overflow: hidden;
    background: var(--canvas-bg);
  }
  .canvas {
    position: relative;
    width: 1200px;
    height: 1000px;
  }
  .lawn-sign {
    position: absolute;
    left: 340px;
    top: 143px;
    width: 548px;
    height: 727px;
    background: var(--sign-bg);
    box-shadow: 12px 14px 10px var(--shadow);
    font-family: "Open Sans", Arial, sans-serif;
    font-weight: 700;
    color: var(--ink);
    text-align: center;
  }
  .brand {
    position: absolute;
    left: 0;
    right: 0;
    top: 34px;
    height: 340px;
    display: flex;
    align-items: center;
    justify-content: center;
    gap: 26px;
  }
  .brand-dot {
    width: 96px;
    height: 96px;
    border-radius: 50%;
    background: var(--accent);
    flex: none;
  }
  .brand-name {
    margin: 0;
    font-size: 112px;
    line-height: 110px;
    letter-spacing: 1px;
    text-align: left;
    color: var(--ink);
    white-space: nowrap;
  }
  .brand-name span {
    display: block;
  }
  .contact-phone {
    position: absolute;
    left: 0;
    right: 0;
    top: 396px;
    margin: 0;
    font-size: 59px;
    line-height: 64px;
    letter-spacing: -0.5px;
    white-space: nowrap;
  }
  .contact-email {
    position: absolute;
    left: 0;
    right: 0;
    top: 463px;
    margin: 0;
    font-size: 29px;
    line-height: 36px;
    white-space: nowrap;
  }
  .services {
    position: absolute;
    left: 0;
    right: 0;
    top: 525px;
    margin: 0;
    padding: 0;
    list-style: none;
    font-size: 33px;
    line-height: 33px;
  }
</style>
</head>
<body>
  <main class="canvas">
    <section class="lawn-sign">
      <div class="brand">
        <span class="brand-dot" aria-hidden="true"></span>
        <p class="brand-name"><span>TIDY</span><span>TURF</span><span>CO</span></p>
      </div>
      <p class="contact-phone">PH: 816-402-7761</p>
      <p class="contact-email">Email: tidyturfco@fernmail.com</p>
      <ul class="services">
        <li>Mowing</li>
        <li>Fertilization</li>
        <li>Aeration</li>
        <li>Bed &amp; tree maintenance</li>
        <li>and more.</li>
      </ul>
    </section>
  </main>
</body>
</html>
```